"Tumbling Pebbles" Mobile 2D Game

We need a mobile design for the main screen of the game (with a popup design to select the ball color), for a Professional IT Team. Our initial game is "Tumbling Pebbles", classic board game for kids and even non kids. We would like to see design that suitable for mobile devices (small and tablet). The main concept of the game will be something similar to this video link: https://www.vidtrovex.com/watch?v=KqP7rLmwZtE

Please be sure the balls inside the game board have readable numbers. Thanks!

Requirements
Must have
• Separate layers for each UI component so it can be exported easily

```html
<!DOCTYPE html>
<html lang="en">
<head>
<meta charset="utf-8">
<title>Tumbling Pebbles – Select the Ball Color</title>
<link href="https://fonts.googleapis.com/css2?family=Luckiest+Guy&display=swap" rel="stylesheet">
<style>
  :root {
    --ink: #0a0a0a;
    --navy-ring: #071624;
    --white: #ffffff;
    --teal: #10a3c3;
    --orange: #f08a10;
    --pink: #f01f8a;
    --lime: #9fd81a;
    --blue: #2e6fe0;
    --purple: #5a2ec8;
    --swatch-forest: #045a48;
    --swatch-teal: #10a3c3;
    --swatch-plum: #4a0f5e;
    --swatch-crimson: #ae0018;
    --swatch-pink: #f597ee;
    --swatch-rust: #b93402;
    --swatch-orange: #ea8722;
    --swatch-gold: #ecc11b;
  }
  * { box-sizing: border-box; margin: 0; padding: 0; }
  html, body { width: 675px; height: 1200px; overflow: hidden; }
  body { font-family: "Luckiest Guy", "Arial Black", sans-serif; }

  .screen {
    position: relative;
    width: 675px;
    height: 1200px;
    overflow: hidden;
  }

  .backdrop {
    position: absolute;
    inset: 0;
    background:
      radial-gradient(circle at 20% 8%, var(--orange) 0 18%, transparent 30%),
      radial-gradient(circle at 85% 5%, var(--pink) 0 12%, transparent 24%),
      radial-gradient(circle at 76% 20%, var(--blue) 0 11%, transparent 20%),
      radial-gradient(circle at 48% 28%, var(--lime) 0 11%, transparent 20%),
      radial-gradient(circle at 20% 30%, var(--pink) 0 9%, transparent 18%),
      radial-gradient(circle at 12% 40%, var(--purple) 0 8%, transparent 16%),
      radial-gradient(circle at 90% 30%, var(--orange) 0 12%, transparent 22%),
      radial-gradient(circle at 20% 63%, var(--blue) 0 10%, transparent 18%),
      radial-gradient(circle at 60% 63%, var(--orange) 0 14%, transparent 24%),
      radial-gradient(circle at 92% 58%, #f7a0b8 0 10%, transparent 20%),
      radial-gradient(circle at 0% 70%, #1aa030 0 8%, transparent 16%),
      radial-gradient(circle at 72% 77%, var(--pink) 0 12%, transparent 22%),
      radial-gradient(circle at 96% 74%, var(--lime) 0 8%, transparent 16%),
      radial-gradient(circle at 35% 76%, #d8b20a 0 9%, transparent 18%),
      radial-gradient(circle at 10% 95%, var(--orange) 0 14%, transparent 26%),
      radial-gradient(circle at 85% 95%, var(--pink) 0 10%, transparent 20%),
      linear-gradient(160deg, #d46a12, #7a3a1a 50%, #b8541a);
    filter: blur(6px);
    transform: scale(1.04);
  }

  .game-title {
    position: absolute;
    left: 0;
    right: 0;
    top: 392px;
    text-align center;
    text-align: center;
    font-weight: 400;
    line-height: 1;
    paint-order: stroke fill;
    -webkit-text-stroke: 26px var(--white);
  }
  .title-line {
    display: block;
    white-space: nowrap;
    paint-order: stroke fill;
  }
  .title-line--top {
    color: var(--ink);
    font-size: 104px;
    letter-spacing: -2px;
    height: 128px;
    padding-top: 10px;
  }
  .title-line--bottom {
    color: var(--teal);
    font-size: 118px;
    letter-spacing: -1px;
    padding-top: 8px;
  }

  .color-picker {
    position: absolute;
    left: 0;
    right: 0;
    top: 866px;
    text-align: center;
  }
  .picker-heading {
    color: var(--white);
    font-size: 48px;
    font-weight: 400;
    line-height: 1.25;
    -webkit-text-stroke: 12px var(--navy-ring);
    paint-order: stroke fill;
    letter-spacing: -1px;
  }

  .swatch-grid {
    position: absolute;
    left: 163px;
    top: 1000px;
    display: grid;
    grid-template-columns: repeat(4, 86px);
    grid-template-rows: repeat(2, 90px);
  }
  .swatch {
    width: 86px;
    height: 86px;
    border-radius: 50%;
    border: 9px solid var(--navy-ring);
    display: flex;
    align-items: center;
    justify-content: center;
  }
  .swatch--forest { background: var(--swatch-forest); }
  .swatch--teal { background: var(--swatch-teal); }
  .swatch--plum { background: var(--swatch-plum); }
  .swatch--crimson { background: var(--swatch-crimson); }
  .swatch--pink { background: var(--swatch-pink); }
  .swatch--rust { background: var(--swatch-rust); }
  .swatch--orange { background: var(--swatch-orange); }
  .swatch--gold { background: var(--swatch-gold); }
  .selected-icon { width: 40px; height: 40px; margin-left: 6px; }
</style>
</head>
<body>
  <main class="screen">
    <div class="backdrop" role="img" aria-label="Blurred photo of many glossy coloured balls in orange, pink, green and blue"></div>

    <h1 class="game-title">
      <span class="title-line title-line--top">Tumbling</span>
      <span class="title-line title-line--bottom">Pebbles</span>
    </h1>

    <section class="color-picker">
      <h2 class="picker-heading">Select the<br>ball color</h2>
    </section>

    <div class="swatch-grid" role="radiogroup" aria-label="Ball color">
      <div class="swatch swatch--forest" role="radio" aria-checked="false" aria-label="Forest green"></div>
      <div class="swatch swatch--teal" role="radio" aria-checked="true" aria-label="Teal">
        <svg class="selected-icon" viewBox="0 0 40 40" aria-hidden="true">
          <polygon points="6,3 38,20 6,37" fill="#ffffff"/>
        </svg>
      </div>
      <div class="swatch swatch--plum" role="radio" aria-checked="false" aria-label="Plum"></div>
      <div class="swatch swatch--crimson" role="radio" aria-checked="false" aria-label="Crimson"></div>
      <div class="swatch swatch--pink" role="radio" aria-checked="false" aria-label="Pink"></div>
      <div class="swatch swatch--rust" role="radio" aria-checked="false" aria-label="Rust"></div>
      <div class="swatch swatch--orange" role="radio" aria-checked="false" aria-label="Orange"></div>
      <div class="swatch swatch--gold" role="radio" aria-checked="false" aria-label="Gold"></div>
    </div>
  </main>
</body>
</html>
```